High School Rowing Club - duplicate example provided

Build web site based on example provided. We would like you to copy the general layout of the Marlowe Brook rowing web site but insert our info (Cedar Vale Northern).
Target Market(s)
High School Parents & Students
Industry/Entity Type
School
Number of Pages Required
5+ page
Font styles to use
Serif
Colors
Designer to choose colors to be used in the design.
Requirements
Must have
- Plug in for payment option (coinlyft?) Parents will be making payments using this options.
- Online Registration Form - Please copy http://marlowebrookrowinghub.example/ registration form inserting the basics. Please do not include their specific items at the bottom.
- Generally, Copy the format of http://marlowebrookrowinghub.example/ to build our site.
Nice to have
- Include the photos we attached. Use "slider" format/style. Include our facebook page on the home/main page: Cedar Vale Northern High School Rowing Team.
- Our content should work for 5 pages (tabs)
- Make sure to copy the green color from our current high school rowing website. http://www.cvnoars.example/

```html
<!DOCTYPE html>
<html lang="en">
<head>
<meta charset="utf-8">
<title>Cedar Vale Northern Rowing</title>
<link href="https://fonts.googleapis.com/css2?family=Oswald:wght@300;400;500;700&display=swap" rel="stylesheet">
<style>
:root{
  --crew-green:#1f6b3a;
  --crew-orange:#e0812a;
  --header-bg:#e4e4e4;
  --ink:#222;
  --white:#fff;
  --footer-bg:#575757;
  --footer-ink:#d8d8d8;
}
*{margin:0;padding:0;box-sizing:border-box}
html,body{width:1200px;height:1064px;overflow:hidden}
body{position:relative;font-family:'Oswald',sans-serif;color:var(--white);background:#2f3438}
a{color:inherit;text-decoration:none}
.abs{position:absolute}

/* header */
.site-header{position:absolute;left:0;top:0;width:1200px;height:96px;background:var(--header-bg);z-index:3}
.social{left:156px;top:20px;font-size:15px;font-weight:500;color:var(--ink);display:flex;align-items:center;gap:8px}
.social-dot{width:16px;height:16px;border-radius:50%;background:var(--crew-green);display:inline-block}
.nav-link{font-size:17px;font-weight:400;color:var(--ink)}
.nav-link.is-active{color:var(--crew-green)}
.nav-link.is-active::after{content:"";position:absolute;left:0;right:-6px;top:30px;height:3px;background:var(--crew-green)}
.register{right:157px;top:20px;font-size:15px;font-weight:500;color:var(--crew-green);text-decoration:underline}
.brand-tab{left:468px;top:0;width:262px;height:158px;z-index:4}
.brand-name{position:absolute;left:0;width:262px;top:40px;text-align:center;font-size:22px;line-height:26px;font-weight:700;color:var(--crew-green);letter-spacing:.5px}

/* hero */
.hero{left:0;top:96px;width:1200px;height:542px;background:linear-gradient(180deg,#6c7478 0%,#59625f 30%,#2a3a2f 60%,#3a3f3a 88%,#4a4c4a 100%)}
.hero-rule{left:232px;width:735px;height:3px;background:var(--white)}
.hero-title{left:0;width:1200px;top:328px;text-align:center;font-size:52px;font-weight:700;line-height:62px;letter-spacing:1px;text-shadow:3px 3px 0 var(--crew-orange)}
.hero-title .sep{font-size:28px;vertical-align:middle;margin:0 12px}
.arrow{width:48px;height:48px;border-radius:50%;display:flex;align-items:center;justify-content:center}
.arrow-prev{left:42px;top:334px;border:2px solid var(--white);background:rgba(0,0,0,.25)}
.arrow-next{left:1110px;top:334px;background:var(--white)}
.dot{top:596px;width:9px;height:9px;border-radius:50%;background:var(--white)}
.dot.is-current{width:13px;height:13px;top:594px;border:2px solid var(--white);background:transparent}

/* info band */
.info-band{left:0;top:638px;width:1200px;height:354px;background:linear-gradient(180deg,#525a60 0%,#3d4449 45%,#2c3236 100%)}
.col-title{top:700px;font-size:19px;font-weight:400}
.col-rule{top:731px;height:2px;background:var(--crew-orange)}
.txt{font-size:14px;font-weight:300;line-height:17.6px}
.subhead{font-size:17px;font-weight:300;line-height:24px}
.link{font-size:15px;font-weight:300}
.link::before{content:"» ";font-weight:400}
.dash{font-size:14px;font-weight:300;letter-spacing:1px}

/* footer */
.site-footer{left:0;top:992px;width:1200px;height:72px;background:var(--footer-bg);color:var(--footer-ink)}
.copyright{left:156px;top:26px;font-size:14px;font-weight:300}
.pay-label{left:810px;top:25px;font-size:15px;font-weight:300}
.pay-name{left:912px;top:24px;font-size:16px;font-weight:500;color:#4a6fb5;display:flex;align-items:center;gap:6px}
.pay-mark{width:12px;height:12px;background:#4a6fb5;display:inline-block}
.to-top{left:1028px;top:26px}
</style>
</head>
<body>

<header class="site-header">
  <div class="abs social">Find Us on: <span class="social-dot"></span></div>
  <nav>
    <a class="abs nav-link is-active" style="left:156px;top:60px">Home</a>
    <a class="abs nav-link" style="left:222px;top:60px">New or Interested</a>
    <a class="abs nav-link" style="left:358px;top:60px">Coaches</a>
    <a class="abs nav-link" style="left:784px;top:53px">Parent Info</a>
    <a class="abs nav-link" style="left:877px;top:53px">Sponsorship</a>
    <a class="abs nav-link" style="left:976px;top:53px">Contact Us</a>
  </nav>
  <a class="abs register">Registration Now!</a>
</header>

<div class="abs brand-tab">
  <svg width="262" height="158" viewBox="0 0 262 158" aria-hidden="true">
    <path d="M0 96 C10 140 60 158 131 158 C202 158 252 140 262 96 L262 0 L0 0 Z" fill="#e4e4e4"/>
  </svg>
  <div class="brand-name">CEDAR VALE<br>NORTHERN<br>ROWING</div>
</div>

<section class="abs hero" role="img" aria-label="Team photo of the rowing club gathered in front of racked racing shells"></section>

<div class="abs hero-rule" style="top:313px"></div>
<h1 class="abs hero-title">CEDAR<span class="sep">●</span>VALE<span class="sep">●</span>NORTHERN<span class="sep">●</span>ROWING</h1>
<div class="abs hero-rule" style="top:402px"></div>

<a class="abs arrow arrow-prev" aria-label="Previous slide">
  <svg width="14" height="14" viewBox="0 0 14 14"><path d="M9 2 L4 7 L9 12" stroke="#fff" stroke-width="2" fill="none"/></svg>
</a>
<a class="abs arrow arrow-next" aria-label="Next slide">
  <svg width="14" height="14" viewBox="0 0 14 14"><path d="M5 2 L10 7 L5 12" stroke="#333" stroke-width="2" fill="none"/></svg>
</a>
<span class="abs dot" style="left:571px"></span>
<span class="abs dot is-current" style="left:587px"></span>
<span class="abs dot" style="left:607px"></span>
<span class="abs dot" style="left:621px"></span>

<section class="abs info-band" role="img" aria-label="Dark rippled lake water"></section>

<h2 class="abs col-title" style="left:156px">Calendar</h2>
<div class="abs col-rule" style="left:156px;width:188px"></div>
<p class="abs txt" style="left:156px;top:753px">2017 CVN Crew Calendar</p>
<a class="abs link" style="left:158px;top:781px">Lantern Cove</a>
<a class="abs link" style="left:158px;top:813px">Harbor Invite</a>
<a class="abs link" style="left:158px;top:846px">Tillman Cup</a>
<a class="abs link" style="left:158px;top:879px">Inland Sprints</a>
<a class="abs link" style="left:158px;top:912px">State Championships</a>

<h2 class="abs col-title" style="left:384px">Latest News</h2>
<div class="abs col-rule" style="left:384px;width:188px"></div>
<p class="abs subhead" style="left:384px;top:751px">Tuesday ---<br>September - 12 - 2017</p>
<p class="abs txt" style="left:384px;top:814px">Fall Conditioning is open to<br>VARSITY rowers only. If you rowed<br>last Spring, you are...</p>
<p class="abs dash" style="left:384px;top:883px">----------</p>
<a class="abs link" style="left:388px;top:912px">View All News</a>

<h2 class="abs col-title" style="left:612px">Crew Photos</h2>
<div class="abs col-rule" style="left:612px;width:188px"></div>
<p class="abs subhead" style="left:612px;top:751px">Photo Album ---</p>
<p class="abs txt" style="left:612px;top:790px">Please click the below link to go to<br>the team photo album.As a remind-<br>er, for the protection of our<br>athletes, no individual names can<br>be used in any photo caption...</p>
<p class="abs dash" style="left:612px;top:888px">----------</p>
<a class="abs link" style="left:614px;top:912px;text-decoration:underline">View Photo Album</a>

<h2 class="abs col-title" style="left:840px">Team Apparel</h2>
<div class="abs col-rule" style="left:840px;width:204px"></div>
<p class="abs txt" style="left:840px;top:753px">All unisuits, novice tanks, and white<br>long sleeve warm-up shirts are<br>included in registration costs.  They<br>will be delivered to your rower<br>before the first regatta.  Other<br>ordered items will ship to me and<br>be delivered as well.</p>
<p class="abs dash" style="left:840px;top:886px">----------</p>
<a class="abs link" style="left:842px;top:910px">Cedar Vale Northern Team</a>

<footer class="abs site-footer">
  <p class="abs copyright">© 2017 Cedar Vale Northern Rowing.  All Rights Reserved</p>
  <p class="abs pay-label">Payment Option</p>
  <div class="abs pay-name"><span class="pay-mark"></span>Coinlyft</div>
  <a class="abs to-top" aria-label="Back to top">
    <svg width="16" height="18" viewBox="0 0 16 18"><path d="M3 9 L8 4 L13 9 M3 15 L8 10 L13 15" stroke="#fff" stroke-width="2" fill="none"/></svg>
  </a>
</footer>

</body>
</html>
```